Car Dealership Vehicle Photo Graphic Overlay

We are looking for a graphic overlay to place on photos of vehicles the dealership lists. I've included several examples to show what we're looking for.

Our color theme is viewable on www.brivanmotorgroup-example.com and the fonts used are included as files in this listing.

We need a photoshop file 4608 by 3456 with a 555.555.5555 format number, www.brivanmotorgroup-example.com and room for our logo, preferably similar to the Motorist's Hamlet format. Info on top, small logo in the corner.

We'd like it to be themed appropriately for vehicle sales but distinct from the two samples as they are the two names in our market who use this type of design.

The completed version should include a .psd file with transparent background which can be added to our batch photoshop action.

```html
<!DOCTYPE html>
<html lang="en">
<head>
<meta charset="utf-8">
<title>Brivan Motor Group Photo Overlay</title>
<link rel="stylesheet" href="https://fonts.googleapis.com/css2?family=Play:wght@700&display=swap">
<style>
  :root {
    --canvas: #ffffff;
    --ink: #0a0a0a;
    --halo: #ffffff;
    --sky-top: #6f8fb0;
    --sky-mid: #c9d4dc;
    --road: #d9dde0;
    --wave-teal: #0f5a7a;
    --wave-shadow: rgba(120,120,120,0.35);
    --car-red: #d4471c;
    --car-blue: #3aa0d0;
  }
  html, body {
    margin: 0;
    padding: 0;
    width: 1200px;
    height: 900px;
    overflow: hidden;
    background: var(--canvas);
  }
  .overlay {
    position: relative;
    width: 1200px;
    height: 900px;
    overflow: hidden;
    background: var(--canvas);
  }
  .header-art {
    position: absolute;
    inset: 0;
  }
  .vehicle-art {
    position: absolute;
    left: 0;
    top: 38px;
    width: 250px;
    height: 172px;
    border-radius: 60px 90px 40px 20px;
    background: radial-gradient(ellipse at 65% 60%, var(--car-red) 0%, #e9a060 30%, var(--car-blue) 62%, rgba(255,255,255,0) 85%);
    opacity: 0.85;
  }
  .contact {
    position: absolute;
    font-family: "Play", sans-serif;
    font-weight: 700;
    color: var(--ink);
    -webkit-text-stroke: 8px var(--halo);
    paint-order: stroke fill;
    white-space: nowrap;
    letter-spacing: -0.5px;
    margin: 0;
  }
  .contact-web {
    left: 242px;
    top: 40px;
    font-size: 36px;
    line-height: 44px;
  }
  .contact-phone {
    left: 283px;
    top: 86px;
    font-size: 46px;
    line-height: 54px;
  }
</style>
</head>
<body>
<div class="overlay">
  <svg class="header-art" width="1200" height="900" viewBox="0 0 1200 900" role="img" aria-label="Night city street photo with light trails, fading into a teal wave">
    <defs>
      <linearGradient id="streetScene" x1="0" y1="0" x2="1" y2="1">
        <stop offset="0" stop-color="#e4e9ec"/>
        <stop offset="0.45" stop-color="var(--sky-mid)"/>
        <stop offset="0.7" stop-color="var(--sky-top)"/>
        <stop offset="1" stop-color="#c8b8a0"/>
      </linearGradient>
      <linearGradient id="sceneFade" x1="0" y1="0" x2="0" y2="1">
        <stop offset="0" stop-color="#ffffff" stop-opacity="0"/>
        <stop offset="1" stop-color="#ffffff" stop-opacity="0.55"/>
      </linearGradient>
      <filter id="soft" x="-10%" y="-50%" width="120%" height="200%">
        <feGaussianBlur stdDeviation="14"/>
      </filter>
      <filter id="softer" x="-10%" y="-50%" width="120%" height="200%">
        <feGaussianBlur stdDeviation="26"/>
      </filter>
    </defs>
    <path class="wave-shadow" d="M0 360 C 250 360, 520 250, 800 225 C 980 212, 1100 240, 1200 262 L1200 300 C 1100 300, 980 270, 800 285 C 520 310, 250 420, 0 420 Z" fill="var(--wave-shadow)" filter="url(#softer)"/>
    <path class="street-scene" d="M0 0 H1200 V235 C 1100 215, 980 195, 800 200 C 520 210, 250 335, 0 335 Z" fill="url(#streetScene)"/>
    <path d="M0 0 H1200 V235 C 1100 215, 980 195, 800 200 C 520 210, 250 335, 0 335 Z" fill="url(#sceneFade)"/>
    <path class="wave-edge" d="M0 330 C 250 332, 520 210, 800 198 C 980 192, 1100 215, 1200 232" fill="none" stroke="var(--wave-teal)" stroke-width="26" filter="url(#soft)"/>
    <path d="M0 348 C 250 348, 520 222, 800 212 C 980 206, 1100 228, 1200 248 L1200 900 L0 900 Z" fill="var(--canvas)"/>
    <path d="M0 348 C 250 348, 520 222, 800 212 C 980 206, 1100 228, 1200 248 L1200 300 C 1100 290, 980 255, 800 262 C 520 275, 250 410, 0 410 Z" fill="var(--wave-shadow)" opacity="0.5" filter="url(#softer)"/>
  </svg>
  <div class="vehicle-art" role="img" aria-label="Illustrated sports car with city skyline"></div>
  <p class="contact contact-web">brivanmotorgroup-example.com</p>
  <p class="contact contact-phone">555.555.5555</p>
</div>
</body>
</html>
```